Bright Arch Group business card

Bright Arch Group is the parent company of Bright Arch Building, Bright Arch Plumbing and Bright Arch Renovating. We require a sophisticated business card that covers all aspects of the building and plumbing space without using told or construction items.

Industry/Entity Type

Construction Company

Contact Information for Business Card

Gareth Pimley
Director
0472915083
gareth@brightarch.com.au
Www.brightarch.com.au

Font styles to use
Serif
Sans Serif

Colors
3176b5
ffce3e
0692cd
34a7d8
fbee3e
faa54b

Requirements
Must have
• Logo on front
• Logo and details on rear.
Nice to have
• Maybe water mark or shadow effect with logo
Should not have
• Tools or any construction associated items

```html
<!DOCTYPE html>
<html lang="en">
<head>
<meta charset="utf-8">
<title>Bright Arch Group – Business Card</title>
<link rel="stylesheet" href="https://fonts.googleapis.com/css2?family=Roboto:wght@400;500&display=swap">
<style>
  :root {
    --bg: #e9e7e3;
    --card: #ffffff;
    --card-shade: #ececec;
    --ink: #1b1b1b;
    --orange: #f2a325;
    --orange-deep: #e08a1c;
    --gold-line: #f1c232;
    --black: #0d0d0d;
  }
  * { margin: 0; padding: 0; box-sizing: border-box; }
  html, body { width: 1200px; height: 1023px; overflow: hidden; background: var(--bg); }
  .canvas {
    width: 1200px; height: 1023px;
    display: flex; flex-direction: column; align-items: center; justify-content: center; gap: 60px;
  }
  .card {
    position: relative; width: 640px; height: 366px;
    background: linear-gradient(135deg, var(--card) 40%, var(--card-shade));
    border-radius: 18px; overflow: hidden;
    box-shadow: 0 6px 18px rgba(0,0,0,.18);
  }
  /* brand name */
  .brand {
    display: flex; align-items: center; gap: 14px;
    font-family: "Roboto", sans-serif; font-weight: 400; color: var(--ink);
    white-space: nowrap;
  }
  .brand .dot { flex: none; border-radius: 50%; background: var(--orange); }
  /* front */
  .front .block { position: absolute; width: 150px; height: 120px;
    background: linear-gradient(135deg, var(--orange), var(--orange-deep)); }
  .front .block-left { left: 40px; bottom: 0; }
  .front .block-right { right: 40px; top: 0; }
  .front .brand { position: absolute; left: 50%; top: 50%; transform: translate(-50%, -50%); font-size: 40px; }
  .front .brand .dot { width: 26px; height: 26px; }
  /* back */
  .back .side-band { position: absolute; left: 0; top: 0; bottom: 0; width: 62px; background: var(--black); }
  .back .side-stripe { position: absolute; left: 0; bottom: 60px; width: 18px; height: 190px;
    background: linear-gradient(180deg, var(--orange-deep), var(--orange)); }
  .back .details { position: absolute; left: 92px; top: 40px;
    font-family: "Roboto", sans-serif; font-size: 15px; color: var(--ink); letter-spacing: .5px; }
  .back .details li { list-style: none; display: flex; align-items: center; gap: 10px; margin-bottom: 10px; }
  .back .details svg { width: 14px; height: 14px; flex: none; }
  .back .rule { position: absolute; left: 82px; right: 200px; top: 150px; height: 1px; background: var(--gold-line); }
  .back .brand { position: absolute; left: 92px; top: 188px; font-size: 32px; }
  .back .brand .dot { width: 20px; height: 20px; }
  .back .person { position: absolute; right: 44px; bottom: 40px; text-align: right; font-family: "Roboto", sans-serif; }
  .back .person .full-name { font-size: 24px; font-weight: 500; color: var(--ink); }
  .back .person .role { font-size: 15px; color: var(--orange); margin-top: 4px; }
  .back .tab { position: absolute; right: 24px; bottom: 0; width: 60px; height: 14px;
    background: var(--orange-deep); border-radius: 4px 4px 0 0; }
</style>
</head>
<body>
<main class="canvas">
  <section class="card front" aria-label="Card front">
    <div class="block block-left"></div>
    <div class="block block-right"></div>
    <div class="brand"><span class="dot"></span>Bright Arch Group</div>
  </section>

  <section class="card back" aria-label="Card back">
    <div class="side-band"></div>
    <div class="side-stripe"></div>
    <ul class="details">
      <li><svg viewBox="0 0 16 16" fill="none" stroke="#f2a325" stroke-width="1.5"><circle cx="8" cy="8" r="7"/><path d="M5.5 4.5l1.5 1.5-1 1.2a6 6 0 0 0 2.8 2.8l1.2-1 1.5 1.5-1 1.2c-3 0-6-3-6-6z"/></svg>0472915083</li>
      <li><svg viewBox="0 0 16 16" fill="none" stroke="#f2a325" stroke-width="1.5"><rect x="1.5" y="3.5" width="13" height="9"/><path d="M1.5 3.5l6.5 5 6.5-5"/></svg>gareth@brightarch.com.au</li>
      <li><svg viewBox="0 0 16 16" fill="none" stroke="#f2a325" stroke-width="1.5"><circle cx="8" cy="8" r="6.5"/><path d="M1.5 8h13M8 1.5c-3 3.5-3 9.5 0 13M8 1.5c3 3.5 3 9.5 0 13"/></svg>www.brightarch.com.au</li>
    </ul>
    <div class="rule"></div>
    <div class="brand"><span class="dot"></span>Bright Arch Group</div>
    <div class="person">
      <div class="full-name">Gareth Pimley</div>
      <div class="role">Director</div>
    </div>
    <div class="tab"></div>
  </section>
</main>
</body>
</html>
```